Vintrel.com- International Goal Achievement Coach Needs Website Design

I need a web design for my new company called Vintrel. I help people who are stuck, people who have a big dream, but don't know how to get there. I help them to break their dreams down into small, manageable steps... and then I'm the "kick in the shin" to get them moving and thriving!

We can all be better- We can all DO better. I inspire people to Ride Onward in the direction of your dreams.

I have uploaded my logo along with some vintage champagne posters. Please use the vintage posters as inspiration. I like the bold, vintage look and feel. I would love the main colors of the design to be black, white and metallic gold. And to follow along this vintage look and feel. Please feel free to use the logo in black or metallic gold or white.

Target Market(s)

websites that I like- janetrulsby.com & hollyp.tv

I would like to also use the vintage champagne photos attached as inspiration as well.

Industry/Entity Type

It Company

Requirements
Must have
• Tabs should include: About, Work With Me, Praise, Giving Back

On the homepage add:
* Sign up for newsletter with space to enter name and email (No click throughs)
* Upcoming Events/Sessions
* Newsletter Posts
* Resources
* Praise Section

* Large photo on top with additional photos throughout the page/site.
Nice to have
• Any additions you can bring to the table would be greatly appreciated.

```html
<!DOCTYPE html>
<html lang="en">
<head>
<meta charset="utf-8">
<title>Vintrel — Goal Achievement Coaching</title>
<link href="https://fonts.googleapis.com/css2?family=Nunito:wght@400;600;700;800&family=Great+Vibes&display=swap" rel="stylesheet">
<style>
:root{
  --gold:#b78a1e;
  --gold-dark:#9a7217;
  --black:#000;
  --white:#fff;
  --canvas:#e8e8e8;
  --text:#333;
  --muted:#555;
  --rule:#e2e2e2;
  --plum:#8c3a5e;
  --quote-bg:#f2ede4;
  --quote-line:#e3dccd;
}
*{box-sizing:border-box;margin:0;padding:0}
html,body{width:1200px;height:1000px;overflow:hidden;background:var(--canvas);font-family:"Nunito",sans-serif;color:var(--text)}
.page{position:absolute;left:249px;top:0;width:703px;height:1000px;background:var(--white)}
.abs{position:absolute}

/* header */
.topbar{left:0;top:0;width:703px;height:33px;background:var(--gold)}
.brand{left:132px;top:0;width:94px;height:49px;background:var(--white);border-radius:0 0 5px 5px;display:flex;align-items:center;justify-content:center;gap:5px;box-shadow:0 1px 3px rgba(0,0,0,.2)}
.brand-mark{width:20px;height:20px;border-radius:50%;background:var(--gold)}
.brand-name{font-size:12px;font-weight:700;color:var(--gold)}
.nav{top:12px;left:396px;display:flex;gap:0;font-size:6px;font-weight:800;color:var(--white);letter-spacing:.2px}
.nav span{margin-right:19px}
.lang{top:12px;left:644px;font-size:5px;color:var(--white);font-weight:600;display:flex;align-items:center;gap:3px}
.lang i{display:inline-block;width:7px;height:5px;background:#c33;border:1px solid #fff}

/* hero */
.hero{left:0;top:33px;width:703px;height:237px;background:radial-gradient(ellipse at 62% 40%,#f3c98a 0%,#d79a48 30%,#8a5418 65%,#3a2108 100%)}
.hero-title{left:134px;top:70px;width:190px;text-align:center;color:var(--white);font-size:24px;line-height:26px;font-weight:700;text-shadow:0 1px 4px rgba(0,0,0,.4)}
.hero-title .script{display:block;font-family:"Great Vibes",cursive;font-weight:400;font-size:34px;line-height:34px;margin-top:2px}

/* signup */
.signup{left:0;top:270px;width:703px;height:42px;background:var(--black)}
.signup-title{left:139px;top:279px;color:var(--white);font-size:11px;font-weight:700}
.signup-title .script{font-family:"Great Vibes",cursive;font-weight:400;font-size:16px}
.signup-sub{left:139px;top:294px;color:var(--gold);font-size:6.5px;font-weight:600}
.signup-sub b{color:var(--white)}
.field{top:284px;width:111px;height:14px;background:var(--white);border-radius:2px;font-size:5.5px;color:#666;padding:4px 5px}
.start{left:516px;top:276px;width:31px;height:31px;border-radius:50%;background:var(--gold);border:1px solid #e0b955;color:var(--white);font-size:6px;font-weight:800;text-align:center;line-height:7px;padding-top:8px}
.start em{font-family:"Great Vibes",cursive;font-style:normal;font-weight:400;font-size:9px}

/* posts */
.post-title{font-size:12.5px;font-weight:700;color:#111}
.tag{height:11px;padding:0 9px 0 6px;background:var(--gold);color:var(--white);font-size:5px;font-weight:700;line-height:11px;clip-path:polygon(0 0,100% 0,88% 50%,100% 100%,0 100%)}
.photo{border-radius:3px}
.copy{font-size:5.6px;line-height:10.3px;color:var(--text)}
.copy a{color:var(--gold);text-decoration:none}
.subhead{font-size:7px;font-weight:700;color:#111}
.share-label{font-size:6px;font-weight:700;color:var(--gold)}
.share{top:672px;height:13px;border:1px solid var(--gold);border-radius:2px;font-size:5.5px;color:var(--gold-dark);display:flex;align-items:center;gap:3px;padding:0 4px}
.share i{font-style:normal;background:var(--gold);color:var(--white);font-size:4px;border-radius:4px;padding:0 2px;line-height:5px}
.rule{height:1px;background:var(--rule)}
.card-title{font-size:7.5px;font-weight:700;color:#111}
.more{font-size:5.5px;font-weight:800;color:var(--gold-dark)}

/* sidebar */
.social{top:334px;width:15px;height:15px;border-radius:50%;background:#a97a3a}
.side-head{font-size:7px;font-weight:700;color:#111}
.events{left:436px;top:385px;width:121px;height:111px;border-radius:10px 14px 14px 10px;overflow:hidden;background:linear-gradient(160deg,#d9c2a4,#b98a80 60%,#8e6a62)}
.events-panel{left:0;top:26px;width:70px;height:85px;background:var(--plum);opacity:.95;color:var(--white);font-size:5px;padding:4px 5px}
.events-panel .lead{font-weight:800;font-size:5px}
.events-panel .sub{font-size:4.5px;opacity:.8}
.ev{border-top:1px solid rgba(255,255,255,.3);margin-top:5px;padding-top:4px;position:relative}
.ev b{font-weight:800}
.ev::after{content:"›";position:absolute;right:0;top:4px;font-size:8px}
.popular{left:436px;top:532px;width:121px;list-style:none}
.popular li{font-size:5.3px;line-height:8.5px;color:var(--gold-dark);margin-bottom:4.5px;padding-left:8px;position:relative}
.popular li::before{content:"›";position:absolute;left:0;color:#999}
.banner{left:436px;width:121px;height:44px;border-radius:3px;background:linear-gradient(90deg,#2b2b2b,#6a6a6a 60%,#bdbdbd)}
.banner-text{left:441px;color:var(--white);font-size:7.5px;font-weight:800;line-height:7.5px}
.banner-text em{font-family:"Great Vibes",cursive;font-style:normal;font-weight:400;font-size:8px}
.quote{left:436px;top:791px;width:118px;height:114px;background:var(--quote-bg);border:1px solid var(--quote-line);border-radius:3px}
.quote-mark{left:444px;top:796px;font-size:22px;color:#cbbfa6;font-family:Georgia,serif}
.quote-text{left:465px;top:799px;width:80px;font-size:5.4px;line-height:10.3px;font-style:italic;color:var(--muted)}
.quote-by{left:466px;top:880px;font-size:5.5px;font-style:italic;font-weight:700;color:#222}

/* footer */
.footer{left:0;top:973px;width:703px;height:27px;background:var(--black);color:var(--white);font-size:5.5px;text-align:center;line-height:27px}
</style>
</head>
<body>
<div class="page">
  <header>
    <div class="abs topbar"></div>
    <div class="abs brand"><span class="brand-mark"></span><span class="brand-name">Vintrel</span></div>
    <nav class="abs nav"><span>ABOUT</span><span>WORK WITH ME</span><span>PRAISE</span><span>GIVING BACK</span></nav>
    <div class="abs lang">Select language <i></i> ▾</div>
  </header>

  <section>
    <div class="abs hero" role="img" aria-label="Photo of a smiling woman with long wavy hair in warm golden sunlight"></div>
    <h1 class="abs hero-title">I help people who have a big <span class="script">Dream</span></h1>
  </section>

  <section>
    <div class="abs signup"></div>
    <div class="abs signup-title">Achieve your <span class="script">Goals</span></div>
    <div class="abs signup-sub">Sign up for weekly updates. <b>It's FREE</b></div>
    <div class="abs field" style="left:272px">Name</div>
    <div class="abs field" style="left:392px">Email</div>
    <div class="abs start">START<br><em>now!</em></div>
  </section>

  <main>
    <h2 class="abs post-title" style="left:133px;top:333px">The Secret to Success</h2>
    <div class="abs tag" style="left:133px;top:355px">8 comments</div>
    <div class="abs photo" style="left:133px;top:375px;width:259px;height:111px;background:linear-gradient(180deg,#dfe3e0,#a6b47a 55%,#6b8a2c)" role="img" aria-label="Photo of a woman in a meadow holding a flowing white scarf"></div>
    <p class="abs copy" style="left:133px;top:493px;width:259px">Sed ut perspiciatis unde omnis iste natus error sit voluptatem accusantium doloremque laudantium, totam rem aperiam, eaque ipsa quae ab illo inventore veritatis et quasi architecto beatae vitae dicta sunt explicabo.</p>
    <p class="abs copy" style="left:133px;top:531px;width:259px">Neque porro quisquam est, qui dolorem ipsum quia dolor sit amet, consectetur, adipisci velit, sed quia non numquam eius modi tempora incidunt ut <a>labore et dolore magnam aliquam</a> quaerat voluptatem.</p>
    <h3 class="abs subhead" style="left:133px;top:562px">The 3 most common self-help questions:</h3>
    <p class="abs copy" style="left:133px;top:579px;width:259px">Lorem ipsum dolor sit amet, consectetur adipisicing elit, sed do eiusmod tempor incididunt ut labore et dolore magna aliqua.</p>
    <p class="abs copy" style="left:133px;top:608px;width:259px">Sed ut perspiciatis unde omnis iste natus error sit voluptatem accusantium doloremque laudantium, totam rem aperiam, eaque ipsa quae ab illo inventore veritatis et quasi architecto beatae vitae dicta sunt explicabo.</p>
    <div class="abs share-label" style="left:133px;top:654px">Sharing is Caring</div>
    <div class="abs share" style="left:133px">Folkpage <i>1.2k</i></div>
    <div class="abs share" style="left:187px">Chirper <i>2.3k</i></div>
    <div class="abs share" style="left:234px">Pinwall <i>800</i></div>
    <div class="abs share" style="left:288px">Linkwork <i>600</i></div>
    <div class="abs rule" style="left:133px;top:707px;width:259px"></div>

    <h2 class="abs card-title" style="left:133px;top:728px">How to Feel More Fulfilled</h2>
    <div class="abs tag" style="left:133px;top:748px">8 comments</div>
    <div class="abs photo" style="left:133px;top:768px;width:111px;height:81px;background:linear-gradient(135deg,#f6e86a,#d9c56a 40%,#7fc7a5)" role="img" aria-label="Photo of a woman stretching her arms in bright sunlight"></div>
    <p class="abs copy" style="left:133px;top:855px;width:111px">Lorem ipsum dolor sit amet, consectetur adipisicing elit, sed do eiusmod tempor incididunt ut labore et dolore magna aliqua.</p>
    <div class="abs more" style="left:133px;top:890px">Read More</div>

    <h2 class="abs card-title" style="left:281px;top:728px">How to handle success</h2>
    <div class="abs tag" style="left:281px;top:748px">8 comments</div>
    <div class="abs photo" style="left:281px;top:768px;width:111px;height:81px;background:linear-gradient(135deg,#eceae4,#b9b3a8 45%,#2b3550)" role="img" aria-label="Photo of a smiling woman seated at a desk"></div>
    <p class="abs copy" style="left:281px;top:855px;width:111px">Lorem ipsum dolor sit amet, consectetur adipisicing elit, sed do eiusmod tempor incididunt ut labore et dolore magna aliqua.</p>
    <div class="abs more" style="left:281px;top:890px">Read More</div>

    <div class="abs rule" style="left:133px;top:918px;width:259px"></div>
    <div class="abs more" style="left:133px;top:936px">⟵ OLDER POSTS</div>
  </main>

  <aside>
    <span class="abs social" style="left:455px"></span>
    <span class="abs social" style="left:478px"></span>
    <span class="abs social" style="left:500px"></span>
    <span class="abs social" style="left:522px"></span>

    <h3 class="abs side-head" style="left:436px;top:367px">Upcoming Events and Sessions</h3>
    <div class="abs events" role="img" aria-label="Photo of a woman with long hair on a sunny beach">
      <div class="abs events-panel">
        <div class="lead">WE CAN ALL BE BETTER</div>
        <div class="sub">we can all do better</div>
        <div class="ev"><b>EVENT #1</b><br>December 20</div>
        <div class="ev"><b>EVENT #2</b><br>December 28</div>
        <div class="ev" style="font-weight:800">VIEW ALL</div>
      </div>
    </div>

    <h3 class="abs side-head" style="left:436px;top:510px">Most Popular</h3>
    <div class="abs rule" style="left:436px;top:522px;width:121px"></div>
    <ul class="abs popular">
      <li>How To Change The World &amp; Live Your Purpose w/ Evan Larke</li>
      <li>The Mental Exercise That Can Turn Wishes Into Reality</li>
      <li>Who Else Influences Your Customers</li>
      <li>Value What You Do. A Must Watch For Artists and Creatives</li>
      <li>Why Smart People Underperform &amp; What To Do About It</li>
    </ul>

    <h3 class="abs side-head" style="left:436px;top:641px">Resources</h3>
    <div class="abs banner" style="top:658px" role="img" aria-label="Black and white photo of a smiling woman"></div>
    <div class="abs banner-text" style="top:666px">I INSPIRE PEOPLE<br>TO RIDE ONWARD<br><em>in the direction<br>of your dreams.</em></div>
    <div class="abs banner" style="top:711px" role="img" aria-label="Black and white photo of a smiling woman"></div>
    <div class="abs banner-text" style="top:724px;font-size:11px;line-height:10px">OVERCOME<br><span style="font-size:6px">FEAR AND SELF DOUBT</span></div>

    <h3 class="abs side-head" style="left:436px;top:772px">Praise</h3>
    <div class="abs rule" style="left:436px;top:784px;width:121px"></div>
    <div class="abs quote"></div>
    <div class="abs quote-mark">“</div>
    <p class="abs quote-text">I would like to thank you for helping me to first visualise, and then to accurately define my business goals. Your business coaching has crystallised, and then confirmed the main reasons for my own personal goals, and my business goals.</p>
    <div class="abs quote-by">- Marla Quinn</div>
  </aside>

  <footer class="abs footer">© 2010 Vintrel.</footer>
</div>
</body>
</html>
```